Health Benefits Association Website Design

The Unified Household Wellspring Alliance (UHWA) is an organization formed for the purpose of providing its members better value for selected health benefits and services. Members can use the association benefits either in conjunction with or independently of other medical insurance they may have. Some of the benefits available include discounted dental and vision care and prescription mail order services. There is no limitation on who can join. This membership will be primarily marketed as a way to enhance the value of a fixed benefit health insurance plan although members do not have to have the insurance plan join the association.

We are seeking a design for a website to be used for consumers to get information about membership and for current members to be able to access their benefits. The website should include:

1) A landing page to provide a description of the UHWA

2) A secondary page that can be duplicated that will:
a. Provide a list of benefits
b. Provide a membership enrollment form
c. Provide a member’s only access page
d. Provide a contact page for more information

We are seeking a modern but conservative design that will reflect value, simplicity and good health. The site design will also need to be compatible for use with mobile phones and tablets.

A copy of the association logo is included with the submission. It will also need to be incorporated into the website design. Layouts of similar association websites have also been included for reference.

Target Market(s)

Ages 25 to 65 unmarried, married with no children, professionals, self-employed, active and healthy

Industry/Entity Type

Health And Wellness

Number of Pages Required

2 page

Font styles to use
Sans Serif

Colors

Designer to choose colors to be used in the design.

Requirements
Must have
• UHWA Logo (attached). Use colors from the logo in the website design.
Nice to have
• Graphics, if used, should convey health and fitness and skew toward a diverse array of adults 25 to 40.

```html
<!DOCTYPE html>
<html lang="en">
<head>
<meta charset="utf-8">
<title>Unified Household Wellspring Alliance</title>
<link href="https://fonts.googleapis.com/css2?family=Josefin+Sans:wght@400;600&family=Lato:wght@400;700&display=swap" rel="stylesheet">
<style>
:root{
  --olive:#9ca24f;
  --olive-dark:#8a9040;
  --yellow:#dfb814;
  --sky-top:#8ccbe8;
  --sky-bottom:#b9d7a2;
  --track:#4a4f55;
  --text:#6a6a6a;
  --ink:#1e1e1e;
  --panel:#eef1ee;
  --white:#ffffff;
}
*{margin:0;padding:0;box-sizing:border-box}
html,body{width:726px;height:1200px;overflow:hidden;background:var(--white)}
body{position:relative;font-family:"Lato",sans-serif;color:var(--text)}
.abs{position:absolute}

/* hero */
.hero{left:0;top:0;width:726px;height:389px;background:linear-gradient(180deg,var(--sky-top) 0%,#a9d3e6 40%,var(--sky-bottom) 72%,var(--track) 86%,#3c4046 100%)}
.hero-photo{left:0;top:0;width:726px;height:389px}
.logo{left:58px;top:5px;width:106px;height:106px;border-radius:50%;background:var(--white);display:flex;align-items:center;justify-content:center;text-align:center;padding:14px}
.logo span{font-family:"Josefin Sans",sans-serif;font-weight:600;font-size:10px;line-height:1.25;color:var(--olive-dark);text-transform:uppercase}
.nav{left:222px;top:18px;height:48px;display:flex;align-items:center;font-family:"Josefin Sans",sans-serif;font-size:11px;color:var(--white)}
.nav a{color:var(--white);text-decoration:none;margin-right:15px}
.nav a.active{width:48px;height:48px;border-radius:50%;background:var(--olive);border:2px solid var(--white);display:flex;align-items:center;justify-content:center;margin-right:6px}
.tagline{left:70px;top:193px;width:248px;height:78px;background:rgba(223,184,20,.92);border-radius:3px;padding:18px 0 0 21px;font-family:"Josefin Sans",sans-serif;font-weight:600;font-size:17.5px;line-height:23px;color:var(--white)}
.dots{left:334px;top:364px;display:flex;gap:6px}
.dots i{width:8px;height:8px;border-radius:50%;background:var(--white);display:block}
.dots i.off{background:transparent;border:1.5px solid var(--white)}

/* welcome */
.welcome-photo{left:28px;top:400px;width:340px;height:272px;background:radial-gradient(ellipse at 50% 55%,#f0d8c6 0%,#dcc6b8 35%,#a7cfc4 65%,#f4f4f4 100%)}
.welcome-title{left:370px;top:446px;font-family:"Josefin Sans",sans-serif;font-size:20px;color:var(--ink)}
.welcome-copy{left:371px;top:480px;width:290px;font-size:9.4px;line-height:15px}
.btn{left:373px;top:585px;width:94px;height:25px;background:var(--olive);color:var(--white);font-size:8.5px;font-weight:700;display:flex;align-items:center;justify-content:center;letter-spacing:.3px}

/* features */
.features{left:0;top:672px;width:726px;height:256px;background:var(--panel)}
.card{top:34px;width:179px;height:187px;box-shadow:0 1px 3px rgba(0,0,0,.2);overflow:hidden}
.card-photo{width:100%;height:100%}
.card-label{position:absolute;left:0;bottom:0;width:100%;height:38px;padding:10px 0 0 16px;font-family:"Josefin Sans",sans-serif;font-size:13px}
.card-health{left:76px}
.card-health .card-photo{background:linear-gradient(160deg,#f2eee8,#e9d6c4 60%,#c9b89a)}
.card-health .card-label{background:rgba(156,162,79,.9);color:var(--white)}
.card-charity{left:272px}
.card-charity .card-photo{background:linear-gradient(180deg,#8c9ca8,#c3a88a 55%,#e89b3c 80%,#4a3a2e)}
.card-charity .card-label{background:rgba(223,184,20,.95);color:var(--white)}
.card-life{left:467px}
.card-life .card-photo{background:linear-gradient(180deg,#2f78c8,#7db4e6 65%,#4f9a2f 90%)}
.card-life .card-label{background:rgba(255,255,255,.82);color:var(--ink)}

/* news */
.news-title{left:76px;top:947px;font-family:"Josefin Sans",sans-serif;font-size:18.5px;color:var(--yellow)}
.news-thumb{width:92px;height:92px;border-radius:50%}
.thumb-forest{left:80px;top:982px;background:radial-gradient(circle,#9fb7a8,#5c7a52 70%,#3f5a3a)}
.thumb-yoga{left:371px;top:984px;background:radial-gradient(circle,#e8b5c0,#b9cfa0 65%,#6f9a56)}
.news-item{width:170px}
.news-item h3{font-family:"Josefin Sans",sans-serif;font-weight:400;font-size:11.5px;color:var(--olive-dark);margin-bottom:6px}
.news-item p{font-size:7.3px;line-height:12.4px;margin-bottom:7px}
.news-item a{font-size:9px;color:#333;text-decoration:none;letter-spacing:.2px}

/* footer */
.footer{left:0;top:1117px;width:726px;height:83px;background:var(--olive)}
.footer-nav{left:78px;top:20px;display:flex;gap:15px;font-size:10px;color:var(--white)}
.copyright{left:78px;top:42px;font-size:7.5px;color:var(--white)}
.social{left:569px;top:20px;display:flex;gap:3px}
.social i{width:18px;height:18px;border-radius:50%;border:1.5px solid var(--white);display:block}
</style>
</head>
<body>

<section class="abs hero">
  <div class="abs hero-photo" role="img" aria-label="Two smiling older adults crouched at the start line of a running track"></div>
  <div class="abs logo"><span>Unified Household Wellspring Alliance</span></div>
  <nav class="abs nav">
    <a class="active">Home</a><a>Benefits</a><a>News</a><a>Charities</a><a>Membership</a><a>Member area</a><a>Enroll</a><a>Contact</a>
  </nav>
  <div class="abs tagline">We Provide Better Health<br>Services &amp; Benefits</div>
  <div class="abs dots"><i class="off"></i><i></i><i></i><i></i></div>
</section>

<div class="abs welcome-photo" role="img" aria-label="Smiling mature couple embracing"></div>
<h1 class="abs welcome-title">Welcome to Our Website</h1>
<p class="abs welcome-copy">Welcome to the Unified Household Wellspring Alliance (UHWA). UHWA was started to be part of a senior-focused charitable organization that is different from other organizations with a similar perspective or mission. UHWA believes a charity should focus on raising money to support its mission, not its leaders. So, none of the UHWA officers or board members receive any compensation.</p>
<div class="abs btn">READ MORE</div>

<section class="abs features">
  <div class="abs card card-health">
    <div class="card-photo" role="img" aria-label="Older couple holding apples"></div>
    <div class="card-label">Health Services</div>
  </div>
  <div class="abs card card-charity">
    <div class="card-photo" role="img" aria-label="Hands forming a heart against a sunset"></div>
    <div class="card-label">Our Chairites</div>
  </div>
  <div class="abs card card-life">
    <div class="card-photo" role="img" aria-label="Family jumping in a green field under blue sky"></div>
    <div class="card-label">Lifestyle Benefits</div>
  </div>
</section>

<h2 class="abs news-title">Latest News</h2>
<div class="abs news-thumb thumb-forest" role="img" aria-label="Woman raising arms in a forest"></div>
<article class="abs news-item" style="left:186px;top:990px">
  <h3>Class aptent taciti sociosqu</h3>
  <p>ad litora torquent per conubia nostra per inceptos hymenaeos Proin nulla arcu nonummy luctus dictum eget fermentum et lorem</p>
  <a>READ MORE</a>
</article>
<div class="abs news-thumb thumb-yoga" role="img" aria-label="Group stretching outdoors"></div>
<article class="abs news-item" style="left:476px;top:990px">
  <h3>Class aptent taciti sociosqu</h3>
  <p>ad litora torquent per conubia nostra per inceptos hymenaeos Proin nulla arcu nonummy luctus dictum eget fermentum et lorem</p>
  <a>READ MORE</a>
</article>

<footer class="abs footer">
  <nav class="abs footer-nav"><span>Home</span><span>Benefits</span><span>News</span><span>Charities</span><span>Membership</span><span>Member area</span><span>Enroll</span><span>Contact</span></nav>
  <p class="abs copyright">© 2017 Company Name &nbsp;All right reserved &nbsp;Term of Use</p>
  <div class="abs social"><i></i><i></i><i></i><i></i></div>
</footer>

</body>
</html>
```